Business Card Design Project

We're looking for a unique business card design that stands out from the rest, using the brand and logo we've already developed.
Two-sided design please.
Brightvane Media (www.brightvanemedia.com.au) is a digitally-focused advertising agency that has produces results-driven campaigns. As a result, we'd like our business card to reflect our innovative approach.
Size, shape, orientation, etc, are all flexible (providing the print costs don't become ridiculous or we have to sit there with tiny scissors!).
Business card should include space for name, title, email, mobile, landline and address.
Logo files uploaded.

```html
<!DOCTYPE html>
<html lang="en">
<head>
<meta charset="UTF-8">
<title>Brightvane Media – Business Card</title>
<link rel="stylesheet" href="https://fonts.googleapis.com/css2?family=Orbitron:wght@500;700&family=Roboto:wght@300;400&display=swap">
<style>
  :root {
    --orange: #f26522;
    --orange-light: #f7941d;
    --black: #231f20;
    --white: #ffffff;
    --backdrop: #ece8e4;
  }
  * { box-sizing: border-box; margin: 0; padding: 0; }
  html, body { width: 1200px; height: 1000px; overflow: hidden; }
  body {
    background: var(--backdrop);
    position: relative;
    font-family: "Roboto", Arial, sans-serif;
  }
  .card {
    position: absolute;
    width: 560px;
    height: 330px;
    overflow: hidden;
    box-shadow: 0 6px 18px rgba(0,0,0,0.18);
  }

  /* Front side */
  .card-front { left: 70px; top: 90px; background: var(--white); }
  .card-front .band-orange {
    position: absolute; left: 0; top: 0; width: 100%; height: 50%;
    background: var(--orange);
  }
  .card-front .brand {
    position: absolute; left: 0; top: 0; width: 100%; height: 100%;
    display: flex; align-items: center; justify-content: center; gap: 18px;
  }
  .card-front .brand-dot {
    width: 34px; height: 34px; border-radius: 50%; background: var(--black);
  }
  .card-front .brand-name {
    font-family: "Roboto", Arial, sans-serif;
    font-weight: 300; font-size: 44px; color: var(--black);
    letter-spacing: 1px;
  }

  /* Back side */
  .card-back { left: 570px; top: 570px; background: var(--orange); }
  .card-back .band-black {
    position: absolute; left: 0; top: 0; width: 100%; height: 132px;
    background: var(--black);
  }
  .card-back .band-stripe {
    position: absolute; left: 0; top: 132px; width: 100%; height: 7px;
    background: var(--orange-light);
  }
  .card-back .brand-name {
    position: absolute; left: 0; width: 100%; top: 42px;
    text-align: center;
    font-family: "Roboto", Arial, sans-serif;
    font-weight: 300; font-size: 40px; color: var(--white);
    letter-spacing: 1px;
  }
  .card-back .person-name {
    position: absolute; left: 150px; top: 160px;
    font-family: "Orbitron", Arial, sans-serif;
    font-weight: 500; font-size: 44px; color: var(--black);
    letter-spacing: 6px;
  }
  .card-back .person-title {
    position: absolute; left: 230px; top: 212px;
    font-family: "Orbitron", Arial, sans-serif;
    font-weight: 700; font-size: 20px; color: var(--black);
    letter-spacing: 2px;
  }
  .card-back .contact {
    position: absolute; left: 300px; top: 250px;
    list-style: none; font-size: 15px; color: var(--white);
    line-height: 30px;
  }
  .card-back .icons {
    position: absolute; left: 24px; top: 232px;
    display: flex; flex-direction: column; gap: 10px;
  }
  .card-back .icon {
    width: 32px; height: 32px; background: var(--white);
    display: flex; align-items: center; justify-content: center;
  }
</style>
</head>
<body>

  <section class="card card-front" aria-label="Card front">
    <div class="band-orange"></div>
    <div class="brand">
      <span class="brand-dot"></span>
      <span class="brand-name">Brightvane Media</span>
    </div>
  </section>

  <section class="card card-back" aria-label="Card back">
    <div class="band-black"></div>
    <div class="band-stripe"></div>
    <div class="brand-name">Brightvane Media</div>
    <div class="person-name">NAME</div>
    <div class="person-title">TITLE</div>
    <ul class="contact">
      <li>EMAIL:</li>
      <li>ADDRESS:</li>
    </ul>
    <div class="icons">
      <span class="icon" aria-label="Mobile">
        <svg width="20" height="20" viewBox="0 0 20 20">
          <rect x="5" y="1.5" width="10" height="17" rx="1.5" fill="none" stroke="#231f20" stroke-width="1.6"/>
          <rect x="7" y="4" width="6" height="5" fill="#231f20"/>
          <circle cx="10" cy="15" r="1.2" fill="#231f20"/>
        </svg>
      </span>
      <span class="icon" aria-label="Landline">
        <svg width="20" height="20" viewBox="0 0 20 20">
          <path d="M5 2 L8 5 L6.5 7.5 C7.5 10 10 12.5 12.5 13.5 L15 12 L18 15 L16 18 C9 17.5 2.5 11 2 4 Z" fill="#231f20"/>
        </svg>
      </span>
    </div>
  </section>

</body>
</html>
```